Logo & Visitenkarte für ein Ingenieurbüro
Zielgruppe
Ich bin freiberuflich als Ingenieurbüro unterwegs. Projekte, Planungen erneuerbare Energien, Verbrauchsanalysen, Beratungen. Keine spezielle Zielgruppe. Grundthemen: Technik, Menschen, Netzwerk Verbinden
Aufgabenstellung
Das Design soll klar, vertrauensvoll, wertig, sysmpatisch sein.
Grundthemen: Technik, Menschen, Netzwerk, Verbinden
Rückseite: QR-Code von mir kommt dann nach Beratung

```html
<!DOCTYPE html>
<html lang="de">
<head>
<meta charset="utf-8">
<title>Jonas Falkenried – Visitenkarte</title>
<link rel="stylesheet" href="https://fonts.googleapis.com/css2?family=Montserrat:wght@400;500;600;700;800&display=swap">
<style>
  :root {
    --stage: #262628;
    --card-dark: #2b2a2d;
    --card-light: #f4f5f7;
    --green: #67b04f;
    --orange: #e08a2c;
    --ink: #2f2f33;
    --ink-soft: #45454a;
  }
  * { box-sizing: border-box; margin: 0; padding: 0; }
  html, body { width: 1200px; height: 1199px; overflow: hidden; }
  body {
    background: var(--stage);
    font-family: "Montserrat", sans-serif;
    display: flex;
    flex-direction: column;
    align-items: center;
    justify-content: center;
    gap: 50px;
  }
  .card {
    width: 880px;
    height: 533px;
    position: relative;
    overflow: hidden;
    box-shadow: 0 12px 30px rgba(0,0,0,.45);
  }

  /* Vorderseite */
  .card--front { background: var(--card-dark); }
  .front-band {
    position: absolute;
    left: 0; top: 218px;
    width: 560px; height: 90px;
    background: var(--green);
    display: flex; align-items: center;
    padding-left: 90px; gap: 16px;
  }
  .front-band .mark-square {
    width: 26px; height: 26px; background: var(--card-dark);
  }
  .front-band .brand-name {
    color: var(--card-dark);
    font-weight: 800;
    font-size: 34px;
    line-height: 1;
    letter-spacing: .5px;
    text-transform: uppercase;
  }
  .front-office {
    position: absolute;
    left: 90px; top: 330px;
    color: var(--green);
    font-weight: 700;
    font-size: 38px;
    letter-spacing: 1px;
  }
  .front-emblem {
    position: absolute;
    right: 30px; top: 60px;
    width: 250px; height: 250px;
  }

  /* Rückseite */
  .card--back { background: var(--card-light); }
  .back-brand {
    position: absolute;
    left: 90px; top: 180px;
    display: flex; align-items: center; gap: 16px;
  }
  .back-brand .mark-square { width: 30px; height: 30px; background: var(--orange); }
  .back-brand .brand-name {
    color: var(--green);
    font-weight: 800;
    font-size: 38px;
  }
  .contact {
    position: absolute;
    left: 490px; top: 110px;
    color: var(--ink);
  }
  .contact-name { font-weight: 700; font-size: 33px; }
  .contact-title {
    font-weight: 500; font-size: 20px; color: var(--ink-soft);
    margin: 2px 0 14px 20px;
  }
  .contact-list { list-style: none; }
  .contact-list li {
    display: flex; align-items: flex-start; gap: 14px;
    font-size: 21px; font-weight: 500; line-height: 28px;
    color: var(--ink-soft);
    margin-bottom: 4px;
  }
  .contact-icon {
    flex: none;
    width: 26px; height: 26px; margin-top: 1px;
    background: var(--green); border-radius: 5px;
    display: flex; align-items: center; justify-content: center;
  }
  .contact-icon svg { width: 16px; height: 16px; }
  .back-band {
    position: absolute;
    left: 0; right: 0; bottom: 50px;
    height: 60px;
    background: var(--green);
    color: #fff;
    display: flex; align-items: center;
    padding-left: 190px;
    font-weight: 500; font-size: 28px; letter-spacing: 1.5px;
  }
</style>
</head>
<body>

  <section class="card card--front" aria-label="Vorderseite">
    <div class="front-band">
      <span class="mark-square"></span>
      <span class="brand-name">Jonas Falkenried</span>
    </div>
    <p class="front-office">INGENIEURBÜRO</p>
    <svg class="front-emblem" viewBox="0 0 250 250" role="img" aria-label="Symbol: Blatt und Blitz in einem Kreis">
      <defs>
        <radialGradient id="emblem-fill" cx="50%" cy="50%" r="50%">
          <stop offset="0%" stop-color="#e08a2c" stop-opacity=".55"/>
          <stop offset="100%" stop-color="#67b04f" stop-opacity=".45"/>
        </radialGradient>
      </defs>
      <circle cx="125" cy="125" r="120" fill="url(#emblem-fill)"/>
    </svg>
  </section>

  <section class="card card--back" aria-label="Rückseite">
    <div class="back-brand">
      <span class="mark-square"></span>
      <span class="brand-name">Falkenried</span>
    </div>

    <div class="contact">
      <p class="contact-name">Jonas Falkenried</p>
      <p class="contact-title">Dipl. Ing. E-Technik</p>
      <ul class="contact-list">
        <li>
          <span class="contact-icon"><svg viewBox="0 0 16 16"><path d="M8 1a5 5 0 0 0-5 5c0 4 5 9 5 9s5-5 5-9a5 5 0 0 0-5-5z" fill="#fff"/></svg></span>
          <span>Brahmsweg 14,<br>58511 Lindental.</span>
        </li>
        <li>
          <span class="contact-icon"><svg viewBox="0 0 16 16"><path d="M3 2l3 0 1 3-2 1c1 2 3 4 5 5l1-2 3 1 0 3c-6 0-11-5-11-11z" fill="#fff"/></svg></span>
          <span>02351 40 12 345</span>
        </li>
        <li>
          <span class="contact-icon"><svg viewBox="0 0 16 16"><rect x="4" y="1" width="8" height="14" rx="1.5" fill="#fff"/><rect x="5.5" y="3" width="5" height="8" fill="#67b04f"/></svg></span>
          <span>0171 204 4321</span>
        </li>
        <li>
          <span class="contact-icon"><svg viewBox="0 0 16 16"><rect x="1.5" y="3.5" width="13" height="9" fill="none" stroke="#fff" stroke-width="1.5"/><path d="M1.5 3.5l6.5 5 6.5-5" fill="none" stroke="#fff" stroke-width="1.5"/></svg></span>
          <span>info@j-falkenried.de</span>
        </li>
        <li>
          <span class="contact-icon"><svg viewBox="0 0 16 16"><circle cx="8" cy="8" r="6.2" fill="none" stroke="#fff" stroke-width="1.4"/><ellipse cx="8" cy="8" rx="2.6" ry="6.2" fill="none" stroke="#fff" stroke-width="1.2"/><path d="M2 8h12" stroke="#fff" stroke-width="1.2"/></svg></span>
          <span>www.j-falkenried.de</span>
        </li>
      </ul>
    </div>

    <div class="back-band">BERATUNG - PLANUNG - PROJEKTE</div>
  </section>

</body>
</html>
```